Vorential Health Posters

Two posters needed to introduce our new package pricing, called our SPARK and GLOW programs. Our current posters are attached, these two new posters should be similar design and layout. The docx attached has what information should be on each poster. (vorentialhealth.com)

```html
<!DOCTYPE html>
<html lang="en">
<head>
<meta charset="utf-8">
<title>Vorential Health – GLOW and SPARK Package Posters</title>
<link href="https://fonts.googleapis.com/css2?family=Exo+2:ital,wght@0,600;0,700;0,800;1,700;1,900&display=swap" rel="stylesheet">
<style>
  :root {
    --backdrop: #a9a9ab;
    --poster: #070707;
    --red: #c4212b;
    --text: #ececec;
    --muted: #d8d8d8;
  }
  * { box-sizing: border-box; margin: 0; padding: 0; }
  html, body { width: 692px; height: 1200px; overflow: hidden; }
  body {
    background: var(--backdrop);
    position: relative;
    font-family: "Exo 2", Arial, sans-serif;
  }
  .poster {
    position: absolute;
    left: 152px;
    width: 389px;
    height: 549px;
    background: var(--poster);
    overflow: hidden;
    box-shadow: 0 3px 8px rgba(0,0,0,.35);
  }
  .poster--glow { top: 36px; }
  .poster--spark { top: 614px; }

  .photo { position: absolute; }
  .poster--glow .photo {
    left: 150px; top: 0; width: 239px; height: 549px;
    background:
      radial-gradient(ellipse 60% 45% at 55% 28%, #4a4a4a 0%, #2a2a2a 45%, rgba(7,7,7,0) 80%),
      radial-gradient(ellipse 50% 30% at 35% 72%, #2b2b2b 0%, rgba(7,7,7,0) 75%);
  }
  .poster--spark .photo {
    left: 0; top: 204px; width: 389px; height: 345px;
    background:
      radial-gradient(ellipse 40% 55% at 30% 45%, #5a5a5a 0%, #333 40%, rgba(20,20,20,0) 80%),
      linear-gradient(180deg, #070707 0%, #262626 18%, #1e1e1e 70%, #0d0d0d 100%);
  }

  .brand {
    position: absolute; left: 38px; top: 42px;
    font-weight: 700; font-size: 21px; letter-spacing: 1px;
    color: var(--red); line-height: 1;
  }
  .title {
    position: absolute; left: 36px;
    font-weight: 900; font-style: italic;
    font-size: 42px; line-height: 36px;
    color: var(--red); letter-spacing: 0.5px;
  }
  .poster--glow .title { top: 149px; }
  .poster--spark .title { top: 103px; }
  .tagline {
    position: absolute; left: 34px;
    font-weight: 600; font-size: 8.5px; color: var(--text);
  }
  .poster--glow .tagline { top: 228px; }
  .poster--spark .tagline { top: 181px; }

  .benefits { position: absolute; list-style: none; }
  .poster--glow .benefits { left: 34px; top: 292px; }
  .poster--spark .benefits { left: 162px; top: 262px; }
  .benefits li {
    display: flex; align-items: center; height: 26px;
    font-weight: 700; font-size: 10px; letter-spacing: 0.3px;
    color: var(--text);
  }
  .benefits svg { width: 18px; height: 18px; margin-right: 14px; flex: none; }

  .powered {
    position: absolute; left: 34px; top: 452px;
    font-weight: 700; font-size: 13px; color: #fff;
  }
  .offer {
    position: absolute; left: 34px; top: 484px;
    font-weight: 700; font-style: italic; font-size: 10px;
    line-height: 13px; color: var(--muted);
  }
  .offer .accent { color: var(--red); }
</style>
</head>
<body>
<svg width="0" height="0" style="position:absolute">
  <defs>
    <symbol id="tick" viewBox="0 0 18 18">
      <rect x="1" y="3" width="14" height="14" fill="none" stroke="#e0e0e0" stroke-width="1"/>
      <path d="M4 10 L8 14 L17 1" fill="none" stroke="#e0e0e0" stroke-width="1.1"/>
    </symbol>
  </defs>
</svg>

<section class="poster poster--glow">
  <div class="photo" role="img" aria-label="Black and white photo of a muscular man's torso holding a dumbbell"></div>
  <div class="brand">VORENTIAL</div>
  <h1 class="title">GLOW<br>PACKAGE</h1>
  <p class="tagline">Burn Fat. Boost Energy. Transform Your Body.</p>
  <ul class="benefits">
    <li><svg><use href="#tick"/></svg>INCREASE FAT LOSS</li>
    <li><svg><use href="#tick"/></svg>BOOST METABOLISM</li>
    <li><svg><use href="#tick"/></svg>IMPROVE SLEEP</li>
    <li><svg><use href="#tick"/></svg>PROTECT MUSCLE MASS</li>
    <li><svg><use href="#tick"/></svg>INCREASE ENERGY</li>
  </ul>
  <p class="powered">Powered by Peptides + TRT</p>
  <p class="offer">One Low Monthly Price — Save BIG Over the Year<br><span class="accent">3 Months FREE</span> When You Stay Committed All Year</p>
</section>

<section class="poster poster--spark">
  <div class="photo" role="img" aria-label="Black and white gym photo of a muscular man lifting a curl bar"></div>
  <div class="brand">VORENTIAL</div>
  <h1 class="title">SPARK<br>PACKAGE</h1>
  <p class="tagline">Gain Muscle. Recover Faster. Maximize Your Strength.</p>
  <ul class="benefits">
    <li><svg><use href="#tick"/></svg>GAIN LEAN MUSCLE MASS</li>
    <li><svg><use href="#tick"/></svg>ACCELERATE RECOVERY</li>
    <li><svg><use href="#tick"/></svg>BOOST STRENGTH</li>
    <li><svg><use href="#tick"/></svg>INCREASE GROWTH HORMONE</li>
    <li><svg><use href="#tick"/></svg>IMPROVE BODY COMPOSITION</li>
    <li><svg><use href="#tick"/></svg>ENHANCE SLEEP &amp; ENERGY</li>
  </ul>
  <p class="powered">Powered by Peptides + TRT</p>
  <p class="offer">One Low Monthly Price — Save BIG Over the Year<br><span class="accent">3 Months FREE</span> When You Stay Committed All Year</p>
</section>
</body>
</html>
```